Fresh Start Body Quest 2017 Poster

We are having a Fresh Start, Body Quest for 2017 at our fitness studio. We need a poster design using the template attached as a reference (Only reference). I have also included our Drovelux logo to put on the poster. Please DO NOT use the graphics in the flyer as we are expecting something much much better :-)
MUST HAVES:
- Size needed 11x17 with bleeding for printing
- .PSD File Format WITH LAYERS (CS3 Compatible)*** A MUST
- Use Drovelux Bootcamps Logo
- Use Information in the attached word doc

```html
<!DOCTYPE html>
<html lang="en">
<head>
<meta charset="UTF-8">
<title>Fresh Start Body Quest 2017 Poster</title>
<link rel="stylesheet" href="https://fonts.googleapis.com/css2?family=Montserrat:wght@400;600;700;800;900&family=Raleway:wght@300;400;500&display=swap">
<style>
  :root {
    --ink: #ffffff;
    --ink-soft: #e6e6e6;
    --accent-blue: #2f8fe0;
    --brand-navy: #1c3d7a;
    --panel-white: #f4f4f4;
    --bg-dark: #0d0d0d;
    --bg-mid: #2a2a2a;
    --rule: #d8d8d8;
    --chrome-light: #ffffff;
    --chrome-mid: #b9bcc0;
    --chrome-dark: #6d7075;
  }
  * { margin: 0; padding: 0; box-sizing: border-box; }
  html, body { width: 783px; height: 1200px; overflow: hidden; background: var(--bg-dark); }
  .poster {
    position: relative;
    width: 783px;
    height: 1200px;
    overflow: hidden;
    font-family: "Raleway", sans-serif;
    color: var(--ink);
    text-align: center;
  }
  .athlete-photo {
    position: absolute; inset: 0;
    background:
      radial-gradient(ellipse 55% 45% at 50% 52%, rgba(120,120,120,0.55), rgba(0,0,0,0) 70%),
      linear-gradient(180deg, #1a1a1a 0%, var(--bg-mid) 45%, #1e1e1e 70%, var(--bg-dark) 100%);
  }
  .shade { position: absolute; inset: 0; background: rgba(0,0,0,0.35); }

  .brand {
    position: absolute; left: 50%; top: 14px; transform: translateX(-50%);
    width: 410px; height: 180px;
    background: var(--panel-white);
    display: flex; align-items: center; justify-content: center;
  }
  .brand-name {
    font-family: "Montserrat", sans-serif; font-weight: 800;
    font-size: 40px; color: var(--brand-navy); letter-spacing: 1px;
    text-transform: uppercase; line-height: 1.1;
  }

  .title {
    position: absolute; top: 238px; left: 0; right: 0;
    font-family: "Montserrat", sans-serif; font-weight: 900;
    font-size: 92px; letter-spacing: 2px; line-height: 1;
    background: linear-gradient(180deg, var(--chrome-light) 0%, var(--chrome-mid) 48%, var(--chrome-dark) 52%, var(--chrome-light) 100%);
    -webkit-background-clip: text; background-clip: text; color: transparent;
  }
  .subtitle {
    position: absolute; top: 340px; left: 0; right: 0;
    font-family: "Montserrat", sans-serif; font-weight: 600;
    font-size: 30px; letter-spacing: 1px;
  }
  .divider { position: absolute; top: 396px; left: 190px; width: 403px; height: 18px; }

  .offer-lead {
    position: absolute; top: 452px; left: 0; right: 0;
    font-size: 27px; font-weight: 400; color: var(--ink-soft);
  }
  .offer-price {
    position: absolute; top: 508px; left: 0; right: 0;
    font-family: "Raleway", sans-serif; font-size: 64px; font-weight: 400;
  }

  .prize { position: absolute; top: 648px; left: 0; right: 0; line-height: 1.1; }
  .prize-amount { font-family: "Montserrat", sans-serif; font-weight: 700; font-size: 78px; color: var(--accent-blue); }
  .prize-label { font-family: "Montserrat", sans-serif; font-weight: 400; font-size: 56px; }
  .prize-line { font-family: "Montserrat", sans-serif; font-weight: 400; font-size: 56px; display: block; }

  .promise {
    position: absolute; top: 905px; left: 0; right: 0;
    font-size: 19px; font-weight: 400;
  }

  .schedule {
    position: absolute; top: 962px; left: 40px; right: 40px; height: 134px;
    border-top: 2px solid var(--rule); border-bottom: 2px solid var(--rule);
    display: flex; align-items: center;
  }
  .schedule-heading {
    width: 285px;
    font-family: "Montserrat", sans-serif; font-weight: 600; font-size: 96px;
    letter-spacing: 2px; line-height: 1;
  }
  .schedule-list {
    border-left: 2px solid var(--rule); padding-left: 18px; height: 100px;
    display: flex; flex-direction: column; justify-content: center;
    text-align: left; list-style: none; font-size: 18px; line-height: 1.3;
  }

  .footer {
    position: absolute; top: 1136px; left: 0; right: 0;
    font-size: 22px; font-weight: 400;
  }
  .footer .site { color: var(--accent-blue); }
</style>
</head>
<body>
<main class="poster">
  <div class="athlete-photo" role="img" aria-label="Dark studio photo of a muscular athlete crouching beside a kettlebell"></div>
  <div class="shade"></div>

  <header class="brand">
    <span class="brand-name">Drovelux<br>Bootcamps</span>
  </header>

  <h1 class="title">FRESH START</h1>
  <h2 class="subtitle">BODY QUEST</h2>

  <svg class="divider" viewBox="0 0 403 18" aria-hidden="true">
    <line x1="0" y1="9" x2="190" y2="9" stroke="#d8d8d8" stroke-width="1.5"/>
    <circle cx="201.5" cy="9" r="5" fill="#ffffff"/>
    <line x1="213" y1="9" x2="403" y2="9" stroke="#d8d8d8" stroke-width="1.5"/>
  </svg>

  <p class="offer-lead">6 Weeks of Training, Nutrition, and Coaching Starting</p>
  <p class="offer-price">just $99!</p>

  <p class="prize">
    <span class="prize-amount">$ 500</span> <span class="prize-label">CASH Prize</span>
    <span class="prize-line">for</span>
    <span class="prize-line">Winner</span>
  </p>

  <p class="promise">In Just 6 Weeks, Transform Your Body And Get In The Best Shape Of Your Life!</p>

  <section class="schedule">
    <h3 class="schedule-heading">TIME</h3>
    <ul class="schedule-list">
      <li>Kick Off Meeting: Thursday, Jan 12th at 7:30 pm</li>
      <li>Start Date: Tuesday, January 17th</li>
      <li>End Date: Saturday, February 25th</li>
      <li>Finale Party March 2nd</li>
    </ul>
  </section>

  <p class="footer">Visit <span class="site">www.droveluxbootcamps.com</span> FOR MORE INFO</p>
</main>
</body>
</html>
```